UHT milk packaging Design, (Package Design and Outer Carton Design)

Create a Packaging Design
We would like to you to design a UHT milk packaging. We would need our brand logo on the box (Solvine or Brackwell). At present, we do not have a logo design, only the brand name. The Name of the product will be "Full Cream Milk", "Skim Milk", "Lite Milk"

We use Quadra Pak packaging,
Dimensions of 1L product: 90mm*58mm*195mm
Dimensions of 250ml product: 63mm*40mm*106mm

It should also include:
Barcode placeholder
Area for ingredients
1L and 250ml

Upload files are photoes of other Quadra Pak packaging

The final design should communicate:
Freshness
Healthy
Modern
Striking

Subsequently, we also have other products packaging that need to be designed, such as muesli, meat, etc

Target Market(s)

family consumption

Font styles to use
Decorative

Requirements
Must have
• Our brand logo (BRACKWELL);
• Make people feel fresh and healthy
Nice to have
• Bright colors;
• Attractive picture

```html
<!DOCTYPE html>
<html lang="en">
<head>
<meta charset="utf-8">
<title>Brackwell Full Cream Milk – 1 liter carton dieline</title>
<link href="https://fonts.googleapis.com/css2?family=Lilita+One&family=Pacifico&family=Roboto+Condensed:wght@400;700&display=swap" rel="stylesheet">
<style>
  :root{
    --blue-deep:#0b4fa8;
    --blue-mid:#1e6fd0;
    --milk:#ffffff;
    --milk-shade:#d9ecfb;
    --brand-red:#e0202a;
    --ribbon:#f5c518;
    --ribbon-text:#1d3f8f;
    --panel-green:#7cc242;
    --panel-pink:#f7c8d2;
    --panel-magenta:#e01a8c;
    --ink:#111;
    --alert:#e43b2a;
  }
  *{box-sizing:border-box;margin:0;padding:0}
  html,body{width:764px;height:1200px;overflow:hidden;background:#fff}
  .canvas{position:relative;width:764px;height:1200px;background:#fff;font-family:"Roboto Condensed",sans-serif}
  .panel{position:absolute;background:linear-gradient(180deg,var(--blue-mid),var(--blue-deep) 60%,var(--blue-mid));overflow:hidden}
  .flap{left:64px;top:42px;width:384px;height:276px}
  .front{left:64px;top:318px;width:384px;height:838px}
  .side{left:448px;top:318px;width:252px;height:838px}

  .brand{position:absolute;display:flex;align-items:center;justify-content:center;gap:8px;left:0;right:0}
  .brand-disc{border-radius:50%;background:var(--milk);flex:none}
  .brand-name{font-family:"Lilita One",sans-serif;color:var(--brand-red);line-height:1;white-space:nowrap}
  .flap .brand{top:130px;transform:rotate(180deg)}
  .flap .brand-disc{width:20px;height:20px}
  .flap .brand-name{font-size:46px}
  .front .brand{top:200px}
  .front .brand-disc{width:24px;height:24px}
  .front .brand-name{font-size:56px}
  .side .brand{top:100px;gap:6px}
  .side .brand-disc{width:14px;height:14px}
  .side .brand-name{font-size:34px}

  .art{position:absolute}
  .drip{left:0;top:0;width:384px;height:150px;background:linear-gradient(180deg,var(--milk) 55%,var(--milk-shade));border-radius:0 0 40px 40px}
  .mascot{left:228px;top:338px;width:156px;height:370px;background:linear-gradient(180deg,#e7f3fd,#9cc7ee);border-radius:78px 78px 20px 20px}
  .splash{left:0;top:640px;width:384px;height:198px;background:radial-gradient(ellipse at 50% 100%,var(--milk) 45%,var(--milk-shade) 70%,transparent 72%)}
  .side .mascot-head{left:164px;top:170px;width:68px;height:80px;border-radius:50%;background:linear-gradient(180deg,#fff,#f2c97a)}

  .badge{position:absolute;border-radius:50%;border:2px solid var(--milk);background:var(--blue-mid);color:var(--milk);font-family:"Pacifico",cursive;display:flex;align-items:center;justify-content:center;text-align:center;line-height:.85}
  .front .badge{left:54px;top:344px;width:80px;height:80px;font-size:19px}
  .side .badge{left:34px;top:187px;width:66px;height:66px;font-size:15px}

  .product{position:absolute;font-family:"Pacifico",cursive;color:var(--milk);line-height:1;white-space:nowrap}
  .front .product{left:40px;top:418px;font-size:66px}
  .side .product{left:60px;top:234px;font-size:44px}

  .claim{position:absolute;text-align:center;color:var(--ribbon-text);font-weight:700}
  .claim .pct{display:block;font-family:"Lilita One",sans-serif;color:#0d2a6e}
  .claim .ribbon{display:inline-block;background:var(--ribbon);padding:1px 10px}
  .claim .fresh{display:block;color:#0d2a6e}
  .front .claim{left:76px;top:530px;width:124px;transform:rotate(-10deg)}
  .front .claim .pct{font-size:20px}
  .front .claim .ribbon{font-size:13px}
  .front .claim .fresh{font-size:11px}
  .side .claim{left:80px;top:304px;width:92px;transform:rotate(-10deg)}
  .side .claim .pct{font-size:13px}
  .side .claim .ribbon{font-size:9px;padding:0 6px}
  .side .claim .fresh{font-size:8px}

  .gda{position:absolute;left:32px;top:766px;display:flex;gap:3px}
  .gda-item{width:29px;height:36px;border:1.5px solid var(--ink);border-radius:6px 6px 12px 12px;background:var(--milk);text-align:center;font-size:7.5px;line-height:1;padding-top:2px}
  .gda-item b{display:block;margin-top:3px;font-size:15px;font-weight:700;border-top:1.5px solid var(--ink);padding-top:2px}
  .volume{position:absolute;left:288px;top:780px;font-family:"Lilita One",sans-serif;color:var(--ink);font-size:22px}
  .volume span{font-size:28px}

  .nutrition{position:absolute;left:27px;top:356px;width:192px;height:294px;background:var(--milk);border:3px solid var(--panel-green);border-radius:14px;padding:7px 8px;font-size:6px;line-height:1.28;color:var(--ink)}
  .nutrition h2{font-size:10.5px;font-weight:700;line-height:1.1}
  .nutrition .row{display:flex;justify-content:space-between;border-bottom:.5px solid #555}
  .nutrition .thick{border-bottom:2.5px solid var(--ink)}
  .nutrition .sub{padding-left:7px}
  .nutrition b{font-weight:700}
  .nutrition .grid{display:grid;grid-template-columns:1fr 1fr;column-gap:4px}
  .nutrition .grid span{border-bottom:.5px solid #999}
  .nutrition .note{font-size:4.6px;margin-top:3px}
  .nutrition .other{margin-top:3px;background:var(--alert);color:var(--milk);font-size:5.6px;padding:1px 3px}
  .ingredients{position:absolute;left:27px;top:668px;width:192px;height:136px;background:var(--panel-pink);border:2.5px solid var(--panel-magenta);border-radius:14px}
</style>
</head>
<body>
<main class="canvas">

  <section class="panel flap">
    <div class="brand"><span class="brand-disc"></span><span class="brand-name">Brackwell</span></div>
  </section>

  <section class="panel front">
    <div class="art drip" role="img" aria-label="Milk dripping down from the top edge"></div>
    <div class="brand"><span class="brand-disc"></span><span class="brand-name">Brackwell</span></div>
    <div class="art mascot" role="img" aria-label="Cartoon cow mascot holding a glass of milk and pouring a milk can"></div>
    <div class="badge">Full<br>Cream</div>
    <div class="product">Milk</div>
    <div class="claim"><span class="pct">100%</span><span class="ribbon">High Quality</span><span class="fresh">Farm Fresh</span></div>
    <div class="art splash" role="img" aria-label="Milk splash across the bottom"></div>
    <div class="gda">
      <div class="gda-item">Energy<b>00</b></div>
      <div class="gda-item">Fat<b>00</b></div>
      <div class="gda-item">Protein<b>00</b></div>
      <div class="gda-item">Fiber<b>00</b></div>
    </div>
    <div class="volume"><span>1</span> liter</div>
  </section>

  <section class="panel side">
    <div class="brand"><span class="brand-disc"></span><span class="brand-name">Brackwell</span></div>
    <div class="art mascot-head" role="img" aria-label="Cartoon cow mascot head"></div>
    <div class="badge">Full<br>Cream</div>
    <div class="product">Milk</div>
    <div class="claim"><span class="pct">100%</span><span class="ribbon">High Quality</span><span class="fresh">Farm Fresh</span></div>

    <div class="nutrition">
      <h2>Nutrition Facts/Datos de Nutrición</h2>
      <div>Serving Size/Tamaño por Porción 4 scoops/cucharadas (34 g)</div>
      <div>Makes 1 cup prepared/Hace 1 taza (8 fl oz/240 mL) preparada</div>
      <div class="row thick"><span>Servings per Container/Porciones por Envase about/aprox. 47</span></div>
      <div class="row"><b>Amount Per Serving / Cantidad por Porción</b></div>
      <div class="row thick"><span><b>Calories/Calorías</b> 160 Calories from Fat/Calorías de Grasa 60</span></div>
      <div class="row"><b>Total Fat/Grasa Total</b><span>7 g</span></div>
      <div class="row sub"><span>Saturated Fat/Grasa Saturada</span><span>2.5 g</span></div>
      <div class="row sub"><span>Trans Fat/Grasa Trans</span><span>0 g</span></div>
      <div class="row sub"><span>Polyunsaturated Fat/Grasa Poliinsaturada</span><span>1.5 g</span></div>
      <div class="row sub"><span>Monounsaturated Fat/Grasa Monoinsaturada</span><span>2.5 g</span></div>
      <div class="row"><b>Cholesterol/Colesterol</b><span>10 mg</span></div>
      <div class="row"><b>Sodium/Sodio</b><span>80 mg</span></div>
      <div class="row"><b>Potassium/Potasio</b><span>240 mg</span></div>
      <div class="row"><b>Total Carbohydrate/Carbohidrato Total</b><span>19 g</span></div>
      <div class="row sub"><span>Dietary Fiber/Fibra Dietética</span><span>1 g</span></div>
      <div class="row sub"><span>Sugars/Azúcares</span><span>13 g</span></div>
      <div class="row thick"><b>Protein/Proteínas</b><span>5 g</span></div>
      <div class="row"><b>% Daily Value*/% Valor Diario*</b></div>
      <div class="grid">
        <span>Protein/Proteínas 33%</span><span>• Vitamin/Vitamina A 10%</span>
        <span>Vitamin/Vitamina C 35%</span><span>• Calcium/Calcio 30%</span>
        <span>Iron/Hierro 20%</span><span>• Vitamin/Vitamina D 15%</span>
        <span>Vitamin/Vitamina E 15%</span><span>• Thiamine/Tiamina 15%</span>
        <span>Niacin/Niacina 20%</span><span>• Vitamin/Vitamina B6 20%</span>
        <span>Folic Acid/Ácido Fólico 20%</span><span>• Biotin/Biotina 10%</span>
        <span>Pantothenic Acid/Ácido Pantoténico 10%</span><span>• Zinc/Zinc 20%</span>
      </div>
      <div class="note">* Percent Daily Values are for children less than 4 years of age.<br>* Los porcentajes de Valores Diarios son para niños menores de 4 años.</div>
      <div class="other">Other nutrients per serving/Otros nutrientes por porción: Vitamin/Vitamina K 5 mcg, Taurine/Taurina 15 mg.</div>
    </div>

    <div class="ingredients"></div>
  </section>

</main>
</body>
</html>
```